Branding website for a Data Science company with 1 product

Branding website for a Data Science company, featuring our main product: Lumoria. The purpose of the website is to get potential clients to get a peek at what we do, but the main purpose is to get them to get in touch with us. The website will not answer all questions. Therefore the contact details and contact form is a must-have .

Target Market(s)

Potential new B2B clients with medium to large websites, application users (behind a login)

Industry/Entity Type

It Company

Coding

Coded - Design and coding required

Number of Pages Required

2 page

Font styles to use
Sans Serif

Colors

Designer to choose colors to be used in the design.

Requirements
Must have
• A contact form and branding a product

```html
<!DOCTYPE html>
<html lang="en">
<head>
<meta charset="utf-8">
<title>Tally Partners — Data Science</title>
<link rel="stylesheet" href="https://fonts.googleapis.com/css2?family=Lato:wght@400;700;900&family=Open+Sans:wght@400;600&family=Roboto:wght@400&display=swap">
<style>
  :root {
    --orange: #f05a28;
    --navy: #0c1c33;
    --navy-deep: #0a1629;
    --ink: #1d1d1d;
    --grey-bg: #ececec;
    --grey-text: #6b6b6b;
    --white: #ffffff;
    --footer-bg: #0d0d0d;
  }
  * { box-sizing: border-box; margin: 0; padding: 0; }
  html, body { width: 1200px; height: 2308px; overflow: hidden; background: var(--white); }
  body { font-family: "Open Sans", Arial, sans-serif; color: var(--ink); position: relative; }

  /* Header */
  .site-header { height: 60px; display: flex; align-items: center; justify-content: space-between; padding: 0 130px 0 130px; background: var(--white); }
  .brand { display: flex; align-items: center; gap: 10px; }
  .brand-dot { width: 22px; height: 22px; border-radius: 50%; background: var(--orange); }
  .brand-name { font-family: "Lato", Arial, sans-serif; font-weight: 400; font-size: 26px; letter-spacing: 1px; color: var(--orange); text-transform: uppercase; }
  .main-nav { display: flex; gap: 28px; }
  .main-nav a { font-family: "Roboto", Arial, sans-serif; font-size: 12.5px; color: #333; text-decoration: none; text-transform: uppercase; letter-spacing: .3px; }
  .main-nav a.is-active { color: var(--orange); }

  /* Hero */
  .hero { position: relative; height: 513px; }
  .hero-photo { position: absolute; inset: 0; background: linear-gradient(100deg, #3b3029 0%, #5a4a3e 30%, #8d8a86 55%, #c9cfcf 75%, #7b8a7a 100%); }
  .hero-title { position: absolute; left: 128px; top: 341px; width: 477px; height: 110px; background: var(--orange); padding: 8px 14px; font-family: "Lato", Arial, sans-serif; font-weight: 900; font-size: 46px; line-height: 47px; color: var(--white); text-transform: uppercase; letter-spacing: -.5px; }

  /* About */
  .about { position: relative; height: 362px; background: radial-gradient(ellipse at 50% 50%, #1a2c45 0%, var(--navy-deep) 75%); text-align: center; color: var(--white); }
  .about-map { position: absolute; inset: 0; }
  .about-inner { position: relative; padding-top: 92px; }
  .section-title { font-family: "Open Sans", Arial, sans-serif; font-weight: 400; font-size: 54px; line-height: 64px; }
  .section-title .accent { color: var(--orange); }
  .about-text { width: 790px; margin: 12px auto 0; font-size: 16px; line-height: 24px; }

  /* Services */
  .services { display: flex; height: 203px; }
  .service { text-align: center; padding-top: 6px; background: var(--grey-bg); }
  .service-advisory { width: 438px; }
  .service-insights { width: 331px; background: var(--orange); color: var(--white); }
  .service-targeting { width: 431px; }
  .service-icon { display: block; margin: 0 auto; height: 108px; }
  .service-title { font-family: "Lato", Arial, sans-serif; font-weight: 700; font-size: 20px; line-height: 24px; margin-top: 2px; }
  .service-text { font-size: 11.5px; line-height: 14px; color: var(--grey-text); width: 280px; margin: 4px auto 0; }
  .service-insights .service-text { color: var(--white); }

  /* Video */
  .video { position: relative; height: 337px; }
  .video-photo { position: absolute; inset: 0; background: linear-gradient(180deg, #6d7a8c 0%, #b58a63 45%, #6b3d20 62%, #c06a2e 78%, #3a2616 100%); }
  .video-play { position: absolute; left: 540px; top: 91px; }
  .video-label { position: absolute; left: 0; right: 0; top: 228px; text-align: center; font-family: "Roboto", Arial, sans-serif; font-size: 19px; color: var(--white); letter-spacing: .5px; }

  /* Contact */
  .contact { position: relative; height: 460px; background: var(--navy); }
  .contact-title { position: absolute; left: 0; right: 0; top: 40px; text-align: center; font-family: "Lato", Arial, sans-serif; font-weight: 700; font-size: 44px; color: var(--white); }
  .field { position: absolute; background: var(--white); border-radius: 4px; font-family: "Roboto", Arial, sans-serif; font-size: 14px; color: #333; padding: 0 16px; display: flex; align-items: center; }
  .field-name { left: 174px; top: 120px; width: 414px; height: 59px; }
  .field-email { left: 606px; top: 120px; width: 414px; height: 59px; }
  .field-phone { left: 174px; top: 195px; width: 414px; height: 59px; }
  .field-subject { left: 606px; top: 195px; width: 414px; height: 59px; }
  .field-message { left: 174px; top: 269px; width: 846px; height: 77px; align-items: flex-start; padding-top: 18px; }
  .submit-button { position: absolute; left: 463px; top: 369px; width: 274px; height: 48px; background: var(--orange); color: var(--white); font-family: "Lato", Arial, sans-serif; font-weight: 700; font-size: 18px; display: flex; align-items: center; justify-content: center; text-transform: uppercase; }

  /* Footer */
  .site-footer { position: relative; height: 373px; background: linear-gradient(90deg, #141414 0%, var(--footer-bg) 50%, #101010 100%); color: var(--white); }
  .footer-col { position: absolute; top: 42px; }
  .footer-col h3 { font-family: "Open Sans", Arial, sans-serif; font-weight: 600; font-size: 23px; line-height: 30px; margin-bottom: 4px; }
  .footer-col a { display: block; color: #e6e6e6; text-decoration: none; font-size: 17px; line-height: 28.5px; }
  .col-company { left: 220px; }
  .col-connect { left: 420px; }
  .col-sitemap { left: 612px; }
  .col-discover { left: 838px; }
  .footer-rule { position: absolute; left: 201px; top: 260px; width: 797px; height: 1px; background: #777; }
  .social-list { position: absolute; left: 495px; top: 281px; display: flex; gap: 5px; }
  .social-item { width: 38px; height: 38px; border-radius: 50%; background: var(--white); }
  .copyright { position: absolute; left: 0; right: 0; top: 330px; text-align: center; font-size: 11px; color: #ddd; }
</style>
</head>
<body>

<header class="site-header">
  <div class="brand">
    <span class="brand-dot"></span>
    <span class="brand-name">Tally Partners</span>
  </div>
  <nav class="main-nav">
    <a href="#" class="is-active">Home</a>
    <a href="#">Who We Are</a>
    <a href="#">What We Do</a>
    <a href="#">Our Products</a>
    <a href="#">Contact</a>
  </nav>
</header>

<section class="hero">
  <div class="hero-photo" role="img" aria-label="Photo of an analyst at a desktop screen showing business charts, colleagues talking in a bright office"></div>
  <h1 class="hero-title">Welcome to<br>Tally Partners</h1>
</section>

<section class="about">
  <div class="about-map" role="img" aria-label="Night-time satellite view of city lights across a continent"></div>
  <div class="about-inner">
    <h2 class="section-title">WHO <span class="accent">ARE</span> WE?</h2>
    <p class="about-text">We believe that every company needs data science and algorithms to stay on top of today's overwhelming speed of innovation. We advise and help to turn your company into a data driven company by making data science comprehensible and usable for everybody in your organization.</p>
  </div>
</section>

<section class="services">
  <article class="service service-advisory">
    <svg class="service-icon" width="100" height="108" viewBox="0 0 100 108" aria-hidden="true">
      <polygon points="50,6 90,29 90,75 50,98 10,75 10,29" fill="#f05a28"/>
      <circle cx="50" cy="52" r="22" fill="none" stroke="#fff" stroke-width="3"/>
      <path d="M36 68 L32 78 L43 72" fill="none" stroke="#fff" stroke-width="3" stroke-linejoin="round"/>
      <polyline points="38,58 46,48 53,55 63,44" fill="none" stroke="#fff" stroke-width="3"/>
    </svg>
    <h3 class="service-title">Advisory</h3>
    <p class="service-text">Data science comes in many flavors. Which one fits your company best? ? Taking all costs, benefits and organizational impact</p>
  </article>
  <article class="service service-insights">
    <svg class="service-icon" width="100" height="108" viewBox="0 0 100 108" aria-hidden="true">
      <g fill="none" stroke="#fff" stroke-width="3.5" stroke-linecap="round">
        <path d="M38 72 C38 62 30 58 30 46 A20 20 0 0 1 70 46 C70 58 62 62 62 72 Z"/>
        <line x1="40" y1="80" x2="60" y2="80"/>
        <line x1="43" y1="88" x2="57" y2="88"/>
        <line x1="50" y1="6" x2="50" y2="16"/>
        <line x1="16" y1="46" x2="6" y2="46"/>
        <line x1="84" y1="46" x2="94" y2="46"/>
        <line x1="24" y1="20" x2="18" y2="14"/>
        <line x1="76" y1="20" x2="82" y2="14"/>
        <line x1="24" y1="66" x2="18" y2="72"/>
        <line x1="76" y1="66" x2="82" y2="72"/>
        <path d="M44 72 L44 56 L50 62 L56 56 L56 72"/>
      </g>
    </svg>
    <h3 class="service-title">Insights</h3>
    <p class="service-text">We can give you the insights you need to manage your business. We can deliver the technology or the voice-over to your business performance.</p>
  </article>
  <article class="service service-targeting">
    <svg class="service-icon" width="110" height="108" viewBox="0 0 110 108" aria-hidden="true">
      <g fill="none" stroke="#f05a28" stroke-width="3">
        <circle cx="55" cy="48" r="40"/>
        <circle cx="55" cy="48" r="30"/>
        <circle cx="55" cy="48" r="20"/>
        <circle cx="55" cy="48" r="10"/>
        <line x1="55" y1="48" x2="88" y2="96"/>
        <polyline points="78,90 82,96 78,102"/>
        <polyline points="84,90 88,96 84,102"/>
      </g>
    </svg>
    <h3 class="service-title">Targeting and optimization</h3>
    <p class="service-text">Data science can be applied on almost every field where there's data. We specialize in marketing and sales intelligence</p>
  </article>
</section>

<section class="video">
  <div class="video-photo" role="img" aria-label="Photo of a riverside city skyline at dusk with a steel footbridge and lights reflecting on the water"></div>
  <svg class="video-play" width="120" height="120" viewBox="0 0 120 120" aria-hidden="true">
    <circle cx="60" cy="60" r="55" fill="none" stroke="#fff" stroke-width="9"/>
    <polygon points="47,34 47,86 88,60" fill="#fff"/>
  </svg>
  <p class="video-label">WATCH VIDEO</p>
</section>

<section class="contact">
  <h2 class="contact-title">CONTACT US NOW</h2>
  <div class="field field-name">Name</div>
  <div class="field field-email">Enter Your Email</div>
  <div class="field field-phone">Phone</div>
  <div class="field field-subject">Subject</div>
  <div class="field field-message">Write Your Message Here..</div>
  <div class="submit-button">Submit Now</div>
</section>

<footer class="site-footer">
  <div class="footer-col col-company">
    <h3>Company</h3>
    <a href="#">About</a><a href="#">Careers</a><a href="#">Legal</a><a href="#">Privacy Policy</a>
  </div>
  <div class="footer-col col-connect">
    <h3>Connect</h3>
    <a href="#">Friendloop</a><a href="#">Snapframe</a><a href="#">Chirpline</a><a href="#">Pinboardly</a>
  </div>
  <div class="footer-col col-sitemap">
    <h3>Site Map</h3>
    <a href="#">Blog</a><a href="#">Companies</a><a href="#">FAQ</a><a href="#">Find A Candidate</a><a href="#">Find A Job</a>
  </div>
  <div class="footer-col col-discover">
    <h3>Discover</h3>
    <a href="#">Newsroom</a><a href="#">Press</a><a href="#">Advertising</a><a href="#">Flight Schools</a><a href="#">Contact</a>
  </div>
  <div class="footer-rule"></div>
  <div class="social-list">
    <span class="social-item"></span><span class="social-item"></span><span class="social-item"></span><span class="social-item"></span><span class="social-item"></span>
  </div>
  <p class="copyright">© Copyright 2017 Data Science All Rights Reserved</p>
</footer>

</body>
</html>
```